Valdorra Holdings Real Estate Company business cards

New business card design, we are generally happy with the basic layout of the existing front of business card, (feel free to change) but require a head shot photo on the back side.

http://www.valdorra.com.au/

Attached logos, and existing business card

------------------------------

Target Market(s)

Real estate

Industry/Entity Type

Real Estate

Contact Information for Business Card

Standard size double sided

Font styles to use
Other font styles liked:
• Futura

Requirements
Must have
• Photo head shot on the back side
Nice to have
• yes
Should not have
• No

```html
<!DOCTYPE html>
<html lang="en">
<head>
<meta charset="utf-8">
<title>Valdorra Holdings – Business Cards</title>
<link rel="stylesheet" href="https://fonts.googleapis.com/css2?family=Libre+Baskerville:wght@400;700&display=swap">
<style>
  :root {
    --backdrop: #2a2a2c;
    --card-white: #f7f7f8;
    --brand-purple: #2d1f5e;
    --brand-orange: #ec8a1d;
    --text-light: #ffffff;
    --photo-tone-a: #c9c9cc;
    --photo-tone-b: #8e8f96;
  }
  html, body {
    margin: 0;
    width: 1200px;
    height: 873px;
    overflow: hidden;
    background: var(--backdrop);
  }
  .stage {
    position: relative;
    width: 1200px;
    height: 873px;
  }
  .card {
    position: absolute;
    top: 277px;
    width: 520px;
    height: 318px;
    background: var(--card-white);
    overflow: hidden;
    font-family: "Libre Baskerville", Georgia, serif;
  }
  .card--front { left: 60px; }
  .card--back { left: 620px; }

  /* Front */
  .front-content {
    position: absolute;
    inset: 0;
    display: flex;
    flex-direction: column;
    align-items: center;
    justify-content: center;
    gap: 18px;
  }
  .wordmark {
    color: var(--brand-purple);
    font-weight: 400;
    letter-spacing: 0.5px;
    white-space: nowrap;
  }
  .wordmark--large { font-size: 36px; }
  .tagline {
    display: flex;
    gap: 26px;
    color: var(--brand-orange);
    font-size: 17px;
    letter-spacing: 1.5px;
  }

  /* Back */
  .back-shapes {
    position: absolute;
    inset: 0;
  }
  .wordmark--small {
    position: absolute;
    left: 28px;
    top: 52px;
    font-size: 26px;
  }
  .headshot {
    position: absolute;
    left: 364px;
    top: 46px;
    width: 124px;
    height: 124px;
    border-radius: 50%;
    border: 4px solid #ffffff;
    box-sizing: border-box;
    background: radial-gradient(circle at 50% 40%, var(--photo-tone-a), var(--photo-tone-b));
  }
  .social-links {
    position: absolute;
    left: 444px;
    top: 190px;
    display: flex;
    gap: 4px;
  }
  .social-links span {
    width: 10px;
    height: 10px;
    background: #e6e6ec;
    border-radius: 2px;
  }
  .person {
    position: absolute;
    left: 28px;
    top: 222px;
    color: var(--text-light);
  }
  .person-name { font-size: 17px; margin: 0; font-weight: 400; }
  .person-title { font-size: 9px; margin: 3px 0 0; font-weight: 700; }
  .contact-list {
    position: absolute;
    left: 28px;
    top: 264px;
    margin: 0;
    padding: 0;
    list-style: none;
    color: var(--text-light);
    font-size: 11px;
  }
  .contact-list li {
    display: flex;
    align-items: center;
    gap: 7px;
    height: 16px;
  }
  .contact-list svg { width: 10px; height: 10px; flex: none; }
</style>
</head>
<body>
<main class="stage">

  <section class="card card--front" aria-label="Business card front">
    <div class="front-content">
      <div class="wordmark wordmark--large">Valdorra Holdings</div>
      <div class="tagline"><span>BUY</span><span>SELL</span><span>RENT</span></div>
    </div>
  </section>

  <section class="card card--back" aria-label="Business card back">
    <svg class="back-shapes" viewBox="0 0 520 318" preserveAspectRatio="none" aria-hidden="true">
      <path d="M0 196 C 110 150, 240 140, 520 150 L520 318 L0 318 Z" fill="var(--brand-orange)"/>
      <path d="M0 220 C 120 170, 250 166, 520 160 L520 318 L0 318 Z" fill="var(--brand-purple)"/>
    </svg>

    <div class="wordmark wordmark--small">Valdorra Holdings</div>

    <div class="headshot" role="img" aria-label="Head shot photo of Marcus Lee, Director"></div>

    <div class="social-links" aria-label="Social media links">
      <span></span><span></span><span></span>
    </div>

    <div class="person">
      <h2 class="person-name">Marcus Lee</h2>
      <p class="person-title">Director</p>
    </div>

    <ul class="contact-list">
      <li>
        <svg viewBox="0 0 10 10" aria-hidden="true"><rect x="2.5" y="0.5" width="5" height="9" rx="1" fill="none" stroke="var(--brand-orange)" stroke-width="1.2"/><circle cx="5" cy="8" r="0.6" fill="var(--brand-orange)"/></svg>
        0412-555-018
      </li>
      <li>
        <svg viewBox="0 0 10 10" aria-hidden="true"><rect x="0.5" y="2" width="9" height="6" fill="var(--brand-orange)"/><path d="M0.5 2 L5 5.5 L9.5 2" fill="none" stroke="var(--brand-purple)" stroke-width="0.8"/></svg>
        marcus.lee@valdorra.com.au
      </li>
      <li>
        <svg viewBox="0 0 10 10" aria-hidden="true"><path d="M4 6 L6 4 M3.2 4.8 L1.8 6.2 a1.4 1.4 0 0 0 2 2 L5.2 6.8 M4.8 3.2 L6.2 1.8 a1.4 1.4 0 0 1 2 2 L6.8 5.2" fill="none" stroke="var(--brand-orange)" stroke-width="1.1" stroke-linecap="round"/></svg>
        www.valdorra.com.au
      </li>
    </ul>
  </section>

</main>
</body>
</html>
```